Legal Journal cover - modern and sylish

We require a cover design for a new, modern and digital legal academic journal. Attached is our logo so you can get an idea of the feel. This academic journal will have several editions per year.Requirements for the cover design:-The feel of the cover is to be modern -In harmony with our logo-While staying uniform and set in its design,
Updates

Colors
ec1f27

Requirements
Must have
• 1) Colour. Each edition will use different colours. (So we will need the source files to be able to continue to do this)
• 2) An image section. We would like to be able to put in different image or photo with each edition. So we need to have a section, most likely in the shape of a strip, that can include a different image or photo each edition. This part is where we can put a different image in for each edition. So this section would need to be able to accommodate different types of images. It could be a single square. Or it could be a line (a strip) that an image or images.
• 3) A title for the edition and volume and number. Like this:
• Volume 34, No 2 (2016): Contemporary Issues in Criminal Law
• I have attached a range of journals I found online to serve as inspiration.

```html
<!DOCTYPE html>
<html lang="en">
<head>
<meta charset="utf-8">
<title>Legal Academic Journal – Edition Covers</title>
<link rel="stylesheet" href="https://fonts.googleapis.com/css2?family=Roboto+Condensed:wght@400;700&display=swap">
<style>
  :root {
    --red: #ec1f27;
    --charcoal: #333335;
    --slate: #5f6062;
    --navy: #172d52;
    --forest: #1c5a2f;
    --ring: #6d6e70;
    --ink-grey: #58595b;
    --sky-light: #ffffff;
    --sky-mid: #d6eef8;
    --sky-deep: #a9d8ee;
  }
  * { box-sizing: border-box; margin: 0; padding: 0; }
  html, body { width: 1200px; height: 480px; overflow: hidden; background: #fff; }
  .showcase {
    position: relative;
    width: 1200px;
    height: 480px;
    overflow: hidden;
    font-family: "Roboto Condensed", Arial, sans-serif;
  }
  .showcase__stripes { position: absolute; inset: 0; }

  .cover {
    position: absolute;
    overflow: hidden;
    background:
      radial-gradient(ellipse 90% 45% at 50% 0%, var(--sky-light) 0%, var(--sky-mid) 55%, var(--sky-deep) 100%);
    box-shadow: 0 6px 18px rgba(0,0,0,.45);
  }
  .cover::after {
    content: "";
    position: absolute;
    left: 0; right: 0; bottom: 0; height: 35%;
    background: radial-gradient(ellipse 80% 90% at 50% 100%, rgba(255,255,255,.7), rgba(255,255,255,0) 70%);
    pointer-events: none;
  }
  .cover--ed1 { left: 53px;  top: 40px; width: 297px; height: 382px; font-size: 9.9px;  --accent: var(--red);    --title: var(--red); }
  .cover--ed2 { left: 382px; top: 95px; width: 236px; height: 306px; font-size: 7.87px; --accent: var(--slate);  --title: var(--red); }
  .cover--ed3 { left: 647px; top: 88px; width: 247px; height: 320px; font-size: 8.2px;  --accent: var(--navy);   --title: var(--navy); }
  .cover--ed4 { left: 922px; top: 88px; width: 246px; height: 318px; font-size: 8.2px;  --accent: var(--forest); --title: var(--forest); }

  .cover__brand {
    position: absolute;
    top: 3.6em; left: 0; right: 0;
    display: flex; align-items: center; justify-content: center; gap: .6em;
    z-index: 2;
  }
  .cover__brand-dot {
    width: 2.9em; height: 2.9em; border-radius: 50%;
    background: var(--ring);
  }
  .cover__brand-name {
    font-weight: 700;
    font-size: 2em;
    letter-spacing: .02em;
    color: var(--red);
  }

  .cover__band {
    position: absolute;
    left: 0; right: 0;
    top: 13.3em; height: 12.6em;
    background: var(--accent);
  }

  .cover__frame {
    position: absolute;
    left: 50%; top: 8.4em;
    width: 22.5em; height: 22.5em;
    margin-left: -11.25em;
    border-radius: 50%;
    background: var(--ring);
    padding: 1em;
    z-index: 1;
  }
  .cover__frame-inner {
    width: 100%; height: 100%;
    border-radius: 50%;
    background: #fff;
    padding: .45em;
  }
  .cover__photo {
    width: 100%; height: 100%;
    border-radius: 50%;
  }
  .cover__photo--scales { background: radial-gradient(circle at 45% 40%, #6a6052 0%, #2e2b28 55%, #141414 100%); }
  .cover__photo--gavel-keys { background: linear-gradient(135deg, #f2f2f2 0%, #d9d9d9 40%, #6b3a26 60%, #3c1f14 100%); }
  .cover__photo--coins { background: radial-gradient(circle at 35% 30%, #9a8a60 0%, #3a3a3a 40%, #0c0c0c 100%); }
  .cover__photo--house { background: radial-gradient(circle at 55% 60%, #c86b4e 0%, #7a3f28 35%, #f1f1f1 75%); }

  .cover__caption {
    position: absolute;
    left: 0; right: 0; top: 32em;
    text-align: center;
    z-index: 2;
  }
  .cover__title {
    font-weight: 700;
    font-size: 1.31em;
    line-height: 1.2;
    color: var(--title);
  }
  .cover__edition {
    margin-top: .37em;
    font-weight: 700;
    font-size: 1.35em;
    line-height: 1.2;
    color: var(--ink-grey);
  }
</style>
</head>
<body>
<main class="showcase">
  <svg class="showcase__stripes" width="1200" height="480" viewBox="0 0 1200 480" aria-hidden="true">
    <polygon points="376,0 632,0 344,480 80,480" fill="var(--red)"/>
    <polygon points="632,0 896,0 616,480 344,480" fill="var(--charcoal)"/>
    <polygon points="896,0 1152,0 888,480 616,480" fill="var(--navy)"/>
    <polygon points="1152,0 1200,0 1200,480 888,480" fill="var(--forest)"/>
  </svg>

  <article class="cover cover--ed1">
    <div class="cover__brand"><span class="cover__brand-dot"></span><span class="cover__brand-name">LEX FORUM</span></div>
    <div class="cover__band"></div>
    <div class="cover__frame"><div class="cover__frame-inner">
      <div class="cover__photo cover__photo--scales" role="img" aria-label="Photo of brass scales of justice, a gavel and a hand signing a document"></div>
    </div></div>
    <div class="cover__caption">
      <h2 class="cover__title">LEGAL ACADEMIC JOURNAL</h2>
      <p class="cover__edition">EDITION 1</p>
    </div>
  </article>

  <article class="cover cover--ed2">
    <div class="cover__brand"><span class="cover__brand-dot"></span><span class="cover__brand-name">LEX FORUM</span></div>
    <div class="cover__band"></div>
    <div class="cover__frame"><div class="cover__frame-inner">
      <div class="cover__photo cover__photo--gavel-keys" role="img" aria-label="Photo of a wooden gavel resting on a computer keyboard"></div>
    </div></div>
    <div class="cover__caption">
      <h2 class="cover__title">LEGAL ACADEMIC JOURNAL</h2>
      <p class="cover__edition">EDITION 2</p>
    </div>
  </article>

  <article class="cover cover--ed3">
    <div class="cover__brand"><span class="cover__brand-dot"></span><span class="cover__brand-name">LEX FORUM</span></div>
    <div class="cover__band"></div>
    <div class="cover__frame"><div class="cover__frame-inner">
      <div class="cover__photo cover__photo--coins" role="img" aria-label="Photo of stacked coins, a spiral notebook and a calculator"></div>
    </div></div>
    <div class="cover__caption">
      <h2 class="cover__title">LEGAL ACADEMIC JOURNAL</h2>
      <p class="cover__edition">EDITION 3</p>
    </div>
  </article>

  <article class="cover cover--ed4">
    <div class="cover__brand"><span class="cover__brand-dot"></span><span class="cover__brand-name">LEX FORUM</span></div>
    <div class="cover__band"></div>
    <div class="cover__frame"><div class="cover__frame-inner">
      <div class="cover__photo cover__photo--house" role="img" aria-label="Photo of a gavel above a small model house"></div>
    </div></div>
    <div class="cover__caption">
      <h2 class="cover__title">LEGAL ACADEMIC JOURNAL</h2>
      <p class="cover__edition">EDITION 4</p>
    </div>
  </article>
</main>
</body>
</html>
```